New, clean letterhead for law firm in Colorado using recently designed logo.

Professional letterhead for established law firm rebranding. We service high end clientele with mostly family law and personal injury cases. Need source files for future changes. Prefer logo at top, names of members and staff in left margin, contact info in footer.

Target Market(s)

High wealth individuals

Contact Information for Business Card

Need options for traditional and square two sided business cards

Font styles to use
Serif

Colors
0555a3

Requirements
Must have
• Our logo; blue, gray, and white; modern feel.
Should not have
• Images of people

```html
<!DOCTYPE html>
<html lang="en">
<head>
<meta charset="utf-8">
<title>Halvorsen Reid Law, LLC — Stationery</title>
<link href="https://fonts.googleapis.com/css2?family=Noto+Serif:wght@400;600;700&display=swap" rel="stylesheet">
<style>
  :root {
    --brand-blue: #1f6bb0;
    --brand-gray: #9a9a9a;
    --ink: #3a3a3a;
    --paper: #ffffff;
    --backdrop: #c5c9cc;
  }
  * { margin: 0; padding: 0; box-sizing: border-box; }
  html, body { width: 1200px; height: 1018px; overflow: hidden; }
  body {
    background: var(--backdrop);
    font-family: "Noto Serif", Georgia, serif;
    color: var(--ink);
    position: relative;
  }
  .sheet { position: absolute; background: var(--paper); overflow: hidden; }

  /* Plain footer band with a thin rule above it */
  .footer-band { position: absolute; left: 0; right: 0; bottom: 0; background: var(--brand-blue); }
  .footer-rule { position: absolute; left: 0; right: 0; height: 2px; background: var(--brand-gray); }

  /* Business card front */
  .card-front { left: 103px; top: 216px; width: 474px; height: 274px; }
  .card-front .footer-band { height: 36px; }
  .card-front .footer-rule { bottom: 42px; }
  .card-front .firm-mark {
    position: absolute; left: 30px; top: 110px; width: 190px;
    text-align: center; color: var(--brand-blue);
    font-weight: 600; font-size: 15px; letter-spacing: 0.06em; line-height: 1.25;
  }
  .dot { display: block; width: 22px; height: 22px; border-radius: 50%;
         background: currentColor; margin: 0 auto 10px; }
  .card-front .divider { position: absolute; left: 237px; top: 82px; width: 1.5px;
                         height: 110px; background: var(--brand-blue); }
  .card-front .details { position: absolute; left: 256px; top: 78px; }
  .person-name { color: var(--brand-blue); font-weight: 700; font-size: 17.5px; line-height: 1.2; }
  .person-role { font-size: 10px; margin-bottom: 8px; }
  .address { font-size: 9.5px; line-height: 13.5px; margin-bottom: 6px; }
  .contact-list { list-style: none; font-size: 9.5px; line-height: 12px; }
  .contact-list li { display: flex; align-items: center; gap: 4px; }
  .contact-list svg { width: 8px; height: 8px; flex: none; fill: var(--brand-blue); }

  /* Business card back */
  .card-back { left: 103px; top: 528px; width: 474px; height: 273px; background: var(--brand-blue); }
  .card-back .firm-mark {
    position: absolute; left: 0; right: 0; top: 92px; text-align: center;
    color: var(--paper); font-weight: 600; font-size: 25px; letter-spacing: 0.06em; line-height: 1.25;
  }
  .card-back .dot { width: 34px; height: 34px; margin-bottom: 14px; }

  /* Letterhead */
  .letterhead { left: 677px; top: 205px; width: 430px; height: 608px; }
  .letterhead .footer-band { height: 30px; }
  .letterhead .footer-rule { bottom: 36px; }
  .letterhead .firm-mark {
    position: absolute; left: 26px; top: 28px; width: 176px; text-align: center;
    color: var(--brand-blue); font-weight: 600; font-size: 14px; letter-spacing: 0.06em; line-height: 1.25;
  }
  .letter-body { position: absolute; left: 26px; top: 141px; width: 383px;
                 font-size: 7.6px; line-height: 12.4px; }
  .letter-body p { text-align: justify; }
  .letter-body .gap { margin-top: 13px; }
  .signature { width: 80px; height: 32px; margin-top: 8px;
               background: linear-gradient(90deg, #e9e9e9, #f6f6f6); }
  .letter-footer { position: absolute; left: 26px; top: 483px; font-size: 7.8px; }
  .letter-footer .address { font-size: 7.8px; line-height: 11.6px; margin-bottom: 3px; }
  .letter-footer .contact-list { font-size: 7.8px; line-height: 11.8px; }
  .letter-footer .contact-list svg { width: 7px; height: 7px; }
</style>
</head>
<body>

<svg width="0" height="0" style="position:absolute">
  <symbol id="icon-phone" viewBox="0 0 10 10"><path d="M2 0.5 L3.6 2.6 L2.8 3.6 C3.4 5 4.8 6.4 6.4 7.2 L7.4 6.4 L9.5 8 L8.4 9.6 C4.4 9.2 0.8 5.6 0.4 1.6 Z"/></symbol>
  <symbol id="icon-fax" viewBox="0 0 10 10"><rect x="2.5" y="0.5" width="5" height="3"/><rect x="0.5" y="3.5" width="9" height="4" rx="0.8"/><rect x="2.5" y="6.5" width="5" height="3"/></symbol>
  <symbol id="icon-mail" viewBox="0 0 10 10"><path d="M0.5 2 H9.5 V8 H0.5 Z M1.3 2.6 L5 5.6 L8.7 2.6" stroke="#fff" stroke-width="0.7"/></symbol>
  <symbol id="icon-web" viewBox="0 0 10 10"><circle cx="5" cy="5" r="4.5"/><path d="M0.5 5 H9.5 M5 0.5 C3 3 3 7 5 9.5 C7 7 7 3 5 0.5" stroke="#fff" stroke-width="0.6" fill="none"/></symbol>
</svg>

<!-- Business card: front -->
<section class="sheet card-front" aria-label="Business card front">
  <div class="firm-mark"><span class="dot"></span>HALVORSEN REID<br>LAW, LLC</div>
  <div class="divider"></div>
  <div class="details">
    <div class="person-name">Daniel Marsh</div>
    <div class="person-role">Co-Founder</div>
    <div class="address">4180 N. Ridge Avenue, Suite<br>210 Denver, CO 80205</div>
    <ul class="contact-list">
      <li><svg><use href="#icon-phone"/></svg>555-201-4830</li>
      <li><svg><use href="#icon-fax"/></svg>555-201-4831</li>
      <li><svg><use href="#icon-mail"/></svg>info@halvorsenreid.com</li>
      <li><svg><use href="#icon-web"/></svg>www.halvorsenreid.com</li>
    </ul>
  </div>
  <div class="footer-rule"></div>
  <div class="footer-band"></div>
</section>

<!-- Business card: back -->
<section class="sheet card-back" aria-label="Business card back">
  <div class="firm-mark"><span class="dot"></span>HALVORSEN REID<br>LAW, LLC</div>
</section>

<!-- Letterhead -->
<section class="sheet letterhead" aria-label="Letterhead">
  <div class="firm-mark"><span class="dot"></span>HALVORSEN REID<br>LAW, LLC</div>

  <div class="letter-body">
    <div>Mr/s<br>First Name and Last Name<br>Company Name<br>Address</div>
    <p>Lorem Ipsum is simply dummy text of the printing and typesetting industry. Lorem Ipsum has been the industry's standard dummy text ever since the 1500s, when an unknown printer took a galley of type and scrambled it to make a type specimen book. It has survived not only five centuries, but also the leap into electronic typesetting, remaining essentially unchanged. It was popularised in the 1960s with the release of Letraset sheets containing Lorem Ipsum passages.</p>
    <p class="gap">he standard chunk of Lorem Ipsum used since the 1500s is reproduced below for those interested. Sections 1.10.32 and 1.10.33 from "de Finibus Bonorum et Malorum" by Cicero are also reproduced in their exact original form, accompanied by English versions from the 1914 translation by H. Rackham. Lorem ipsum dolor sit amet, consectetur adipiscing elit, sed do eiusmod tempor incididunt ut labore et dolore magna aliqua.</p>
    <p class="gap">It is a long established fact that a reader will be distracted by the readable content of a page when looking at its layout. The point of using Lorem Ipsum is that it has a more-or-less normal distribution of letters, as opposed to using 'Content here, content here', making it look like readable English. Many desktop publishing packages and web page editors now .</p>
    <div class="gap">Your Sincerely,</div>
    <div class="signature" role="img" aria-label="Handwritten signature"></div>
  </div>

  <div class="letter-footer">
    <div class="address">4180 N. Ridge Avenue, Suite<br>210 Denver, CO 80205</div>
    <ul class="contact-list">
      <li><svg><use href="#icon-phone"/></svg>555-201-4830</li>
      <li><svg><use href="#icon-fax"/></svg>555-201-4831</li>
      <li><svg><use href="#icon-mail"/></svg>info@halvorsenreid.com</li>
      <li><svg><use href="#icon-web"/></svg>www.halvorsenreid.com</li>
    </ul>
  </div>

  <div class="footer-rule"></div>
  <div class="footer-band"></div>
</section>

</body>
</html>
```